A online shop for solid wood need a Stationary design

A new online shop (in Austria and Germany) for solid wood and steel furniture (feldberg-formwerk) needs a Stationay design (letterhead, business card, envelope etc...). Dining tables, coffee tables, TV furniture and similar furniture will be sold. Everything will be custom made.

```html
<!DOCTYPE html>
<html lang="en">
<head>
<meta charset="utf-8">
<title>Feldberg Formwerk – Business Card</title>
<link href="https://fonts.googleapis.com/css2?family=Roboto:wght@400;500;700&display=swap" rel="stylesheet">
<style>
  :root {
    --brand-red: #e8222e;
    --brand-red-deep: #e3141c;
    --brand-red-light: #ee3944;
    --ink: #1a1a1a;
    --text-grey: #5d5d5d;
    --rule-grey: #d2d2d2;
    --paper: #ffffff;
    --backdrop: #dcdcdc;
  }
  * { margin: 0; padding: 0; box-sizing: border-box; }
  html, body {
    width: 1200px; height: 1200px; overflow: hidden;
    background: var(--backdrop);
    font-family: "Roboto", Arial, sans-serif;
  }
  .canvas { position: relative; width: 1200px; height: 1200px; }
  .card {
    position: absolute; left: 263px; width: 684px; height: 392px;
    border-radius: 24px; overflow: hidden;
  }
  .card-front { top: 165px; background: var(--paper); }
  .card-back {
    top: 653px;
    background: linear-gradient(45deg, var(--brand-red-deep) 0%, var(--brand-red) 50%, var(--brand-red-light) 100%);
  }

  .wordmark {
    position: absolute; display: flex; flex-direction: column; align-items: center;
    font-weight: 700; text-transform: uppercase; letter-spacing: 3px;
    line-height: 1.1; text-align: center;
  }
  .wordmark .mark-square { width: 74px; height: 74px; margin-bottom: 20px; }
  .card-front .wordmark { left: 66px; width: 260px; top: 110px; color: var(--brand-red); font-size: 30px; }
  .card-front .mark-square { background: var(--brand-red); }
  .card-back .wordmark { left: 0; width: 684px; top: 96px; color: var(--paper); font-size: 36px; }
  .card-back .mark-square { background: var(--paper); width: 96px; height: 96px; }

  .divider {
    position: absolute; left: 335px; top: 84px; width: 1px; height: 235px;
    background: var(--rule-grey);
  }
  .contact { position: absolute; left: 368px; top: 89px; color: var(--text-grey); }
  .contact .person-name { color: var(--brand-red); font-size: 23px; font-weight: 500; line-height: 1.2; }
  .contact .person-role { color: var(--ink); font-size: 16px; font-weight: 500; margin-top: 1px; }
  .contact .address { font-size: 15.5px; line-height: 19px; margin-top: 18px; }
  .contact .lines { list-style: none; margin-top: 12px; font-size: 15.5px; }
  .contact .lines li { display: flex; align-items: center; height: 19.5px; }
  .contact .lines svg { width: 13px; height: 13px; margin-right: 9px; fill: var(--brand-red); flex: none; }
</style>
</head>
<body>
<main class="canvas">
  <section class="card card-front" aria-label="Business card front">
    <div class="wordmark">
      <span class="mark-square"></span>
      <span>Feldberg<br>Formwerk</span>
    </div>
    <div class="divider"></div>
    <div class="contact">
      <p class="person-name">Jonas Reiter</p>
      <p class="person-role">President</p>
      <p class="address">2148 Lindenhof Lane<br>Greenfield, Oregon 40318</p>
      <ul class="lines">
        <li><svg viewBox="0 0 16 16"><path d="M3 1l3 3-1.5 2c1 2 3 4 5 5L11.5 9.5l3 3-2 2.5C7 14 2 9 1 3z"/></svg>418-630-2751</li>
        <li><svg viewBox="0 0 16 16"><path d="M4 0h8v16H4zM5.5 1.5v11h5v-11z"/></svg>418-507-9134</li>
        <li><svg viewBox="0 0 16 16"><path d="M4 1h8v4H4zM1 6h14v6h-2v3H3v-3H1zM5 10v3h6v-3z"/></svg>418-294-6082</li>
        <li><svg viewBox="0 0 16 16"><path d="M1 3h14v10H1zM2.5 4.5L8 9l5.5-4.5z"/></svg>name@feldbergformwerk.com</li>
        <li><svg viewBox="0 0 16 16"><circle cx="8" cy="8" r="7"/></svg>www.feldbergformwerk.com</li>
      </ul>
    </div>
  </section>

  <section class="card card-back" aria-label="Business card back">
    <div class="wordmark">
      <span class="mark-square"></span>
      <span>Feldberg<br>Formwerk</span>
    </div>
  </section>
</main>
</body>
</html>
```